Webbanner-Design für Blog rund um das Thema Immobilie
Zielgruppe
Wir sind ein Blog rund um das Thema Immobilie mit Fokus auf Hausverwaltung und ergänzen unser Angebot aktuell um ein kostenpflichtiges Branchenverzeichnis. https://www.wohnobjekt-kompass.example/
Aufgabenstellung
Sofern sinnvoll, Farbgestaltung des Blogs beibehalten.
Es werden folgende Elemente in einem einheitlichen Stil benötigt:
1. Ein neues Logo für den Blog. Von Stil her gerne wie das bestehende Logo.
2. Ein Trustelement für Kunden, die im Branchenverzeichnis eingetragen sind mit Text 'Eingetragen auf Wohnobjekt-Kompass.example'
3. Werbeanzeige (jeweils: 300x250, 728x90, 300x600) mit Text 'Eintrag im Verzeichnis sichern. Sichtbar werden. Ganz einfach neue Kunden gewinnen.'
4. Werbeanzeige (jeweils: 300x250, 728x90, 300x600) mit Text 'Lassen Sie sich von neuen Kunden finden. Mit einem Eintrag in unserem Branchenverzeichnis.'
5. Werbeanzeige (jeweils: 300x250, 728x90, 300x600) mit Text 'Zielgerichtet werben? Jetzt Eintrag im Verzeichnis sichern!'
6. Werbeanzeige (jeweils: 300x250, 728x90, 300x600) mit Text 'Sie möchten von wechselwilligen Eingentümern gefunden werden? Jetzt Eintrag im Verzeichnis sichern!'
7. Werbeanzeige (jeweils: 300x250, 728x90, 300x600) mit Text 'Lassen Sie sich von Eigentümern finden. Brancheneintrag schon ab € 14,90 monatlich.'
8. Werbeanzeige (jeweils: 300x250, 728x90, 300x600) mit Text 'Die eigene Sichtbarkeit als Verwalter erhöhen? Einfach ins Branchenbuch eintragen lassen.'
9. Werbeanzeige (jeweils: 300x250, 728x90, 300x600) mit Text 'Finden Sie den passenden Anbieter für Ihre Immobilie. Schnell und kostenlos. Zum Branchenverzeichnis.'
10. Werbeanzeige (jeweils: 300x250, 728x90, 300x600) mit Text 'Das spezialisierte Branchenverzeichnis rund um die Immobilie! - 250+ Städte - 3.500+ Dienstleister - einfach suchen und finden'
11. Werbeanzeige (jeweils: 300x250, 728x90, 300x600) mit Text 'Unzufrieden mit der Hausverwaltung? Einfach eine Alternative im Verzeichnis finden!'
12. Werbeanzeige (jeweils: 300x250, 728x90, 300x600) mit Text 'Sie möchten eine Immobilie verkaufen? Finden Sie den passenden Makler in unserem Verzeichnis!'

```html
<!DOCTYPE html>
<html lang="de">
<head>
<meta charset="utf-8">
<title>Werbebanner – Eintrag im Verzeichnis</title>
<link rel="stylesheet" href="https://fonts.googleapis.com/css2?family=Roboto:wght@400;500&display=swap">
<style>
  :root {
    --brand-green: #15812f;
    --ad-bg: #dbe0ea;
    --ad-bg-light: #e4e8ef;
    --text-dark: #222426;
    --frame: #1a1a1a;
    --white: #ffffff;
    --key-light: #eef0f4;
    --key-shadow: #a9adb6;
  }
  * { box-sizing: border-box; margin: 0; padding: 0; }
  html, body {
    width: 994px; height: 1200px; overflow: hidden;
    background: var(--white);
    font-family: "Roboto", Arial, sans-serif;
  }
  .canvas { position: relative; width: 994px; height: 1200px; }

  .ad {
    position: absolute;
    transform-origin: 0 0;
    transform: scale(0.845);
    border: 1px solid var(--frame);
    background: var(--ad-bg);
    overflow: hidden;
    color: var(--text-dark);
  }
  .ad--rect { left: 358px; top: 84px; width: 300px; height: 250px; }
  .ad--leader { left: 177px; top: 396px; width: 728px; height: 90px; }
  .ad--sky { left: 358px; top: 573px; width: 300px; height: 600px; }

  .ad__brand {
    position: absolute; left: 0; top: 0;
    background: var(--white);
    display: flex; align-items: center; gap: 7px;
    color: var(--brand-green);
    font-weight: 400; line-height: 1.3;
  }
  .brand__square { width: 10px; height: 10px; background: var(--brand-green); flex: none; }

  .ad--rect .ad__brand { width: 100%; height: 84px; padding-left: 22px; font-size: 13px; }
  .ad--leader .ad__brand { width: 149px; height: 100%; padding-left: 16px; font-size: 12.5px; }
  .ad--sky .ad__brand { width: 100%; height: 112px; padding-left: 22px; font-size: 14px; }

  .ad__visual {
    position: absolute; right: 0; bottom: 0;
    background: radial-gradient(ellipse at 70% 60%, var(--key-light) 0%, var(--ad-bg-light) 45%, rgba(219,224,234,0) 75%),
                linear-gradient(160deg, rgba(219,224,234,0) 40%, var(--key-shadow) 100%);
  }
  .ad--rect .ad__visual { width: 160px; height: 110px; }
  .ad--leader .ad__visual { width: 190px; height: 90px; }
  .ad--sky .ad__visual { width: 240px; height: 210px; }

  .ad__copy { position: absolute; font-weight: 400; }
  .ad--rect .ad__copy { left: 18px; top: 98px; width: 270px; font-size: 18px; line-height: 26px; }
  .ad--leader .ad__copy { left: 166px; top: 20px; font-size: 15px; line-height: 26px; white-space: nowrap; }
  .ad--sky .ad__copy { left: 33px; top: 198px; width: 250px; font-size: 25px; line-height: 36px; font-weight: 500; }

  .ad__cta {
    position: absolute;
    width: 125px; height: 34px;
    background: var(--brand-green); color: var(--white);
    border-radius: 2px;
    display: flex; align-items: center; justify-content: center;
    font-size: 13px; font-weight: 500; text-decoration: none;
  }
  .ad--rect .ad__cta { left: 157px; top: 200px; }
  .ad--leader .ad__cta { left: 578px; top: 28px; }
  .ad--sky .ad__cta { left: 33px; top: 422px; }
</style>
</head>
<body>
<main class="canvas">

  <section class="ad ad--rect" aria-label="Anzeige 300 x 250">
    <div class="ad__brand"><span class="brand__square"></span><span>Wohnobjekt<br>Kompass</span></div>
    <div class="ad__visual" role="img" aria-label="Schlüsselbund mit zwei silbernen Sicherheitsschlüsseln"></div>
    <p class="ad__copy">Eintrag im Verzeichnis sichern.<br>Sichtbar werden.<br>Ganz einfach neue Kunden gewinnen.</p>
    <a class="ad__cta" href="https://www.wohnobjekt-kompass.example/">mehr erfahren</a>
  </section>

  <section class="ad ad--leader" aria-label="Anzeige 728 x 90">
    <div class="ad__brand"><span class="brand__square"></span><span>Wohnobjekt<br>Kompass</span></div>
    <div class="ad__visual" role="img" aria-label="Schlüsselbund mit zwei silbernen Sicherheitsschlüsseln"></div>
    <p class="ad__copy">Eintrag im Verzeichnis sichern.<br>Sichtbar werden. Ganz einfach neue Kunden gewinnen.</p>
    <a class="ad__cta" href="https://www.wohnobjekt-kompass.example/">mehr erfahren</a>
  </section>

  <section class="ad ad--sky" aria-label="Anzeige 300 x 600">
    <div class="ad__brand"><span class="brand__square"></span><span>Wohnobjekt<br>Kompass</span></div>
    <div class="ad__visual" role="img" aria-label="Schlüsselbund mit zwei silbernen Sicherheitsschlüsseln"></div>
    <p class="ad__copy">Eintrag im Verzeichnis sichern. Sichtbar werden. Ganz einfach neue Kunden gewinnen.</p>
    <a class="ad__cta" href="https://www.wohnobjekt-kompass.example/">mehr erfahren</a>
  </section>

</main>
</body>
</html>
```